KT Hollin's Brochure - Panelform Systems

Hello,
We have an example of very simple brochure (attached below). We would like you to make it better. More sophisticated. More professional looking. All of the info in the document needs to go in the brochure.
Please let me know if you can execute. I will be happy to send over photos, logos etc, once I know.

```html
<!DOCTYPE html>
<html lang="en">
<head>
<meta charset="utf-8">
<title>KT Hollin's Brochure – Quality Control &amp; Design Assist</title>
<link rel="stylesheet" href="https://fonts.googleapis.com/css2?family=Montserrat:wght@400;500;600;700;800&family=Oswald:wght@400;500&display=swap">
<style>
  :root {
    --bg: #e4e6e9;
    --navy: #0f2a5e;
    --navy-deep: #0b1f4d;
    --blue: #1f4a8c;
    --blue-mid: #2a5a9c;
    --sky: #5aa9ea;
    --sky-light: #7cc0f2;
    --pill: #8ccaf5;
    --paper: #f1f2f4;
    --white: #ffffff;
    --ink-blue: #163f80;
  }
  * { margin: 0; padding: 0; box-sizing: border-box; }
  html, body { width: 1200px; height: 953px; overflow: hidden; background: var(--bg); }
  body { position: relative; font-family: "Montserrat", sans-serif; }

  .spread {
    position: absolute; left: 40px; top: 103px;
    width: 1120px; height: 746px; display: flex;
    box-shadow: 0 18px 40px rgba(0,0,0,0.18);
  }
  .page { position: relative; width: 560px; height: 746px; overflow: hidden; }

  /* Left page */
  .page--quality { background: #2a3646; }
  .chamber-photo {
    position: absolute; inset: 0;
    background: linear-gradient(160deg, #3b4554 0%, #55606e 35%, #2d3b55 65%, #4b4a44 100%);
  }
  .brand-mark {
    position: absolute; color: var(--white);
    font-weight: 700; font-size: 15px; letter-spacing: 1.5px; white-space: nowrap;
  }
  .page--quality .brand-mark { left: 45px; top: 52px; }
  .page-title {
    position: absolute; font-weight: 800; letter-spacing: -0.5px; color: var(--white);
  }
  .page-title .accent { color: var(--sky); }
  .page--quality .page-title { left: 45px; top: 112px; font-size: 36px; }
  .tag {
    position: absolute; left: 52px; top: 160px; width: 193px; height: 35px;
    background: var(--sky); color: var(--white);
    font-family: "Oswald", sans-serif; font-size: 12px; letter-spacing: 1.6px;
    display: flex; align-items: center; justify-content: center;
  }
  .tag-frame {
    position: absolute; left: 45px; top: 155px; width: 206px; height: 46px;
    border: 1px solid rgba(255,255,255,0.75);
  }
  .standards-panel {
    position: absolute; left: 340px; top: 361px; width: 220px; height: 338px;
    background: var(--navy-deep);
  }
  .badge {
    position: absolute; left: 24px; top: 20px; width: 163px; height: 66px;
    border: 1.5px solid var(--sky); border-radius: 14px;
    display: flex; align-items: center; gap: 10px; padding-left: 16px;
  }
  .badge-icon { width: 40px; height: 30px; }
  .badge-figure { color: var(--sky-light); font-weight: 800; font-size: 30px; line-height: 1; letter-spacing: -1px; }
  .badge-caption { color: var(--sky-light); font-weight: 700; font-size: 6.5px; letter-spacing: 0.4px; margin-top: 3px; }
  .standards-list { position: absolute; left: 30px; top: 108px; list-style: none; }
  .standards-list li {
    position: relative; padding-left: 22px; margin-bottom: 14px;
    color: #dfe7f3; font-size: 9px; line-height: 15px; letter-spacing: 0.7px;
  }
  .standards-list li::before {
    content: ""; position: absolute; left: 0; top: 6px; width: 6px; height: 6px; background: var(--white);
  }
  .page-number {
    position: absolute; color: var(--white); font-style: italic; font-weight: 700; font-size: 16px;
  }
  .page--quality .page-number { left: 480px; top: 707px; padding-left: 8px; border-left: 1px solid rgba(255,255,255,0.7); }

  /* Right page */
  .page--design { background: var(--blue); }
  .intro {
    position: absolute; left: 0; top: 0; width: 560px; height: 261px;
    background: linear-gradient(135deg, #2e5b9a 0%, #1f4686 60%, #1a3d7a 100%);
  }
  .page--design .brand-mark { left: 47px; top: 50px; }
  .page--design .page-title { left: 47px; top: 100px; font-size: 33px; }
  .intro-text {
    position: absolute; left: 47px; top: 160px; width: 480px;
    color: var(--white); font-size: 11.6px; line-height: 27px; letter-spacing: 0.9px;
  }
  .intro-text em { color: var(--sky-light); font-style: italic; }
  .intro-text strong { color: var(--sky-light); font-weight: 500; }
  .collab-band {
    position: absolute; left: 0; top: 261px; width: 560px; height: 230px; background: var(--paper);
  }
  .team-photo {
    position: absolute; left: 15px; top: 11px; width: 351px; height: 204px;
    background: linear-gradient(160deg, #c9ccd3 0%, #3a4fa0 45%, #8d8f96 100%);
  }
  .resources { position: absolute; left: 388px; top: 33px; width: 145px; }
  .resources-kicker { color: var(--sky); font-weight: 800; font-size: 13px; letter-spacing: 0.8px; line-height: 14px; }
  .resources-heading { color: var(--ink-blue); font-weight: 800; font-size: 18px; letter-spacing: 1px; line-height: 20px; margin-bottom: 6px; }
  .resources-list { list-style: none; }
  .resources-list li {
    color: var(--ink-blue); font-size: 11px; letter-spacing: 0.5px;
    padding: 4px 0 5px; border-bottom: 1px dashed #8fb0d8;
  }
  .resources-list li:last-child { border-bottom: none; }
  .tools { position: absolute; left: 0; top: 491px; width: 560px; height: 255px; background: linear-gradient(180deg, #163a78, #1e4686); }
  .tools-heading { position: absolute; left: 32px; top: 26px; color: var(--sky-light); font-weight: 800; font-size: 17px; letter-spacing: 0.5px; }
  .pill {
    position: absolute; height: 22px; background: var(--pill); color: var(--ink-blue);
    font-size: 11px; letter-spacing: 0.6px; border-radius: 4px 10px 4px 10px;
    display: flex; align-items: center; justify-content: center;
    box-shadow: 0 2px 0 rgba(0,0,0,0.15);
  }
  .page--design .page-number { left: 278px; top: 700px; padding-bottom: 2px; border-bottom: 1px solid rgba(255,255,255,0.6); }
</style>
</head>
<body>
<main class="spread">
  <section class="page page--quality">
    <div class="chamber-photo" role="img" aria-label="Photo of a tall curtain wall panel inside the air and water test chamber in the factory"></div>
    <div class="brand-mark">KT HOLLIN'S</div>
    <h1 class="page-title">Quality <span class="accent">Control</span></h1>
    <div class="tag-frame"></div>
    <div class="tag">AIR AND WATER TEST CHAMBER</div>
    <aside class="standards-panel">
      <div class="badge">
        <svg class="badge-icon" viewBox="0 0 40 30" aria-hidden="true">
          <path d="M2 28 V12 L12 6 V12 L22 6 V12 L32 6 V28 Z" fill="none" stroke="#7cc0f2" stroke-width="2.5" stroke-linejoin="round"/>
          <rect x="6" y="2" width="4" height="8" fill="#7cc0f2"/>
        </svg>
        <div>
          <div class="badge-figure">100%</div>
          <div class="badge-caption">FACTORY ASSEMBLED</div>
        </div>
      </div>
      <ul class="standards-list">
        <li>Temperature Controlled<br>Clean Environment</li>
        <li>Lean Standard Work<br>Training and Certification</li>
        <li>Sealant Manufacture<br>Certification</li>
        <li>Rigorous Quality<br>Inspections</li>
        <li>5% of Completed Units<br>Tested for Air &amp; Water</li>
      </ul>
    </aside>
    <div class="page-number">5</div>
  </section>

  <section class="page page--design">
    <div class="intro">
      <div class="brand-mark">KT HOLLIN'S</div>
      <h2 class="page-title">Design <span class="accent">Assist</span></h2>
      <p class="intro-text">Through our <em>Charrette Process</em>, we work together with the entire team to identify the <strong>Owner's needs</strong>, the <strong>Architect's design intent</strong>, and the <strong>Contractor's schedule and budget</strong>.</p>
    </div>
    <div class="collab-band">
      <div class="team-photo" role="img" aria-label="Photo of the project team meeting around a conference table with laptops and a whiteboard"></div>
      <div class="resources">
        <div class="resources-kicker">RESOURCES</div>
        <div class="resources-heading">WE PROVIDE</div>
        <ul class="resources-list">
          <li>Curtain Wall Designer</li>
          <li>Architect</li>
          <li>Structural Engineer</li>
          <li>Estimator</li>
          <li>Project Manager</li>
        </ul>
      </div>
    </div>
    <div class="tools">
      <h3 class="tools-heading">TOOLS WE USE</h3>
      <div class="pill" style="left:33px;top:65px;width:150px;">Strata for BIM Models</div>
      <div class="pill" style="left:217px;top:65px;width:136px;">Decision Matrix</div>
      <div class="pill" style="left:381px;top:65px;width:136px;">Mind Map</div>
      <div class="pill" style="left:33px;top:103px;width:150px;">Elevation Map</div>
      <div class="pill" style="left:217px;top:103px;width:136px;">Document Tracking</div>
      <div class="pill" style="left:381px;top:103px;width:136px;">Budget Updates</div>
      <div class="pill" style="left:33px;top:141px;width:150px;">Product Samples</div>
    </div>
    <div class="page-number">6</div>
  </section>
</main>
</body>
</html>
```